Company providing Business Management Services needs modern business card

The business provides services like tender preparation, bank submissions, business health checks, financial and admin support. We want to portray 'Trust', 'Strength' and 'Support'.
2 styles of logo in various formats have been uploaded.
Looking for easy to understand, yet sophisticated and stand out from the crowd.

Target Market(s)

Small and Medium sized businesses

Industry/Entity Type

Business

Contact Information for Business Card

Name - Daniel Vesterby, Description - Manager, Phone - 0472 915 603, Email - danielvesterby@kpwholdingsgroup.example, Work description - Business Management Services.

Requirements
Must have
• Logo

```html
<!DOCTYPE html>
<html lang="en">
<head>
<meta charset="utf-8">
<title>KPW Holdings Group – Business Card</title>
<link rel="stylesheet" href="https://fonts.googleapis.com/css2?family=Open+Sans:wght@400;600;700&family=Arimo:wght@700&display=swap">
<style>
  :root {
    --card-black: #1b1b1b;
    --ink: #262626;
    --white: #ffffff;
    --orange: #e8731f;
    --blue: #2e4c9b;
    --purple: #7a2e8c;
    --green: #2fa043;
    --bg-light: #fbfbfb;
    --bg-edge: #c4c4c4;
  }
  * { margin: 0; padding: 0; box-sizing: border-box; }
  html, body { width: 1200px; height: 966px; overflow: hidden; }
  body {
    position: relative;
    font-family: "Open Sans", Arial, sans-serif;
    background: radial-gradient(ellipse 720px 560px at 640px 420px, var(--bg-light) 0%, #e6e6e6 55%, var(--bg-edge) 100%);
  }
  .brand-header {
    position: absolute; top: 58px; left: 0; width: 1200px;
    display: flex; justify-content: center; align-items: center; gap: 10px;
  }
  .brand-header .brand-square { width: 18px; height: 18px; background: var(--orange); }
  .brand-header .brand-name { font-size: 32px; font-weight: 700; color: var(--ink); letter-spacing: 0.5px; }

  .card {
    position: absolute; width: 506px; height: 306px;
    background: var(--card-black); border-radius: 20px; overflow: hidden;
  }
  .card-front { left: 99px; top: 206px; }
  .card-back { left: 594px; top: 545px; }

  .card-waves { position: absolute; left: 0; top: 0; width: 506px; height: 306px; }

  .card-logo { position: absolute; display: flex; align-items: center; gap: 10px; }
  .card-logo .brand-square { background: var(--orange); }
  .card-logo .brand-name { color: var(--white); font-weight: 700; }
  .card-front .card-logo { left: 20px; top: 64px; }
  .card-front .brand-square { width: 16px; height: 16px; }
  .card-front .brand-name { font-size: 24px; }
  .card-back .card-logo { left: 0; width: 506px; top: 132px; justify-content: center; }
  .card-back .brand-square { width: 22px; height: 22px; }
  .card-back .brand-name { font-size: 32px; }

  .holder { position: absolute; right: 17px; top: 23px; text-align: right; }
  .holder-name { font-size: 16.5px; font-weight: 700; color: var(--white); line-height: 22px; }
  .holder-role { font-size: 13px; color: var(--orange); line-height: 18px; }

  .contacts { position: absolute; left: 24px; top: 167px; list-style: none; }
  .contacts li {
    display: flex; align-items: center; gap: 6px;
    font-size: 13.5px; color: var(--white); height: 22.5px;
  }
  .contacts svg { width: 13px; height: 13px; flex: none; }

  .services { position: absolute; right: 16px; top: 197px; list-style: none; text-align: right; }
  .services li { font-size: 13.5px; color: var(--white); line-height: 18.8px; }
  .services .mark { color: var(--orange); margin-left: 7px; }

  .side-label {
    position: absolute; width: 300px; text-align: center;
    font-family: "Arimo", Arial, sans-serif; font-weight: 700; font-size: 28px; color: var(--ink);
  }
  .label-front { left: 202px; top: 534px; }
  .label-back { left: 697px; top: 863px; }
</style>
</head>
<body>
  <header class="brand-header">
    <span class="brand-square"></span>
    <span class="brand-name">KPW Holdings Group</span>
  </header>

  <section class="card card-front">
    <svg class="card-waves" viewBox="0 0 506 306" aria-hidden="true">
      <path fill="var(--blue)" d="M150,306 C260,292 330,232 400,180 C440,152 478,143 506,140 L506,306 Z"/>
      <path fill="var(--orange)" d="M40,256 C170,285 290,222 380,168 C430,142 470,134 506,130 L506,138 C472,141 436,150 392,178 C300,236 180,290 40,256 Z"/>
      <path fill="var(--purple)" d="M0,232 C70,256 170,266 282,250 C200,282 90,292 0,280 Z"/>
      <path fill="var(--green)" d="M0,276 C30,290 58,300 76,306 L0,306 Z"/>
    </svg>

    <div class="card-logo">
      <span class="brand-square"></span>
      <span class="brand-name">KPW Holdings Group</span>
    </div>

    <div class="holder">
      <p class="holder-name">Daniel Vesterby</p>
      <p class="holder-role">Manager</p>
    </div>

    <ul class="contacts">
      <li>
        <svg viewBox="0 0 13 13" aria-hidden="true"><rect x="0.5" y="2.5" width="12" height="8" fill="var(--orange)"/><path d="M0.5,2.5 L6.5,7 L12.5,2.5" fill="none" stroke="var(--card-black)" stroke-width="1"/></svg>
        danielvesterby@kpwholdingsgroup.example
      </li>
      <li>
        <svg viewBox="0 0 13 13" aria-hidden="true"><circle cx="6.5" cy="6.5" r="5.5" fill="none" stroke="var(--orange)" stroke-width="1.4"/><ellipse cx="6.5" cy="6.5" rx="2.3" ry="5.5" fill="none" stroke="var(--orange)" stroke-width="1.1"/><line x1="1" y1="6.5" x2="12" y2="6.5" stroke="var(--orange)" stroke-width="1.1"/></svg>
        www.kpwholdingsgroup.example
      </li>
      <li>
        <svg viewBox="0 0 13 13" aria-hidden="true"><path d="M1,5 C1,2 12,2 12,5 L10,6 L9,4.5 L4,4.5 L3,6 Z" fill="var(--orange)"/><rect x="2.5" y="7" width="8" height="5" rx="1" fill="var(--orange)"/></svg>
        0472 915 603
      </li>
    </ul>

    <ul class="services">
      <li>Admin Support<span class="mark">«</span></li>
      <li>Bank Submission<span class="mark">«</span></li>
      <li>Tender Preparation<span class="mark">«</span></li>
      <li>Financial Assessments<span class="mark">«</span></li>
      <li>Business health checks<span class="mark">«</span></li>
    </ul>
  </section>
  <p class="side-label label-front">Front Side</p>

  <section class="card card-back">
    <div class="card-logo">
      <span class="brand-square"></span>
      <span class="brand-name">KPW Holdings Group</span>
    </div>
  </section>
  <p class="side-label label-back">Back Side</p>
</body>
</html>
```